Voice Over IP Service

Create a 1-2 page brochure for our voice over IP phone system service.

The color pallet should use these colors..
#e23232 red
#636466 Grey
#434445 Dark grey

```html
<!DOCTYPE html>
<html lang="en">
<head>
<meta charset="utf-8">
<title>Kestrel Voice – Hosted VoIP Brochure</title>
<link rel="stylesheet" href="https://fonts.googleapis.com/css2?family=Montserrat:wght@400;500;600;700;800&family=Roboto+Condensed:wght@400;600&display=swap">
<style>
:root{
  --red:#e23232;
  --grey:#636466;
  --dark:#434445;
  --stage:#a3a3a3;
  --ink:#2b2b2c;
  --white:#ffffff;
  --orange:#f26b3a;
  --amber:#f2b01e;
  --green:#1f9e4f;
  --teal:#12a3b8;
  --navy:#1f4f78;
}
*{margin:0;padding:0;box-sizing:border-box}
html,body{width:1200px;height:873px;overflow:hidden;background:var(--stage)}
body{position:relative;font-family:'Montserrat',sans-serif;color:var(--ink)}
.page{position:absolute;top:131px;width:471px;height:610px;background:var(--white);overflow:hidden}
.page--front{left:106px}
.page--back{left:623px}

.brand{position:absolute;display:flex;align-items:center;gap:4px;font-family:'Montserrat',sans-serif;font-weight:700;font-size:13px;color:var(--red);letter-spacing:-.2px}
.brand__dot{width:9px;height:9px;border-radius:50%;background:var(--red)}

/* front */
.hero-photo{position:absolute;left:0;top:0;width:471px;height:360px;
  background:linear-gradient(100deg,#ffffff 0%,#f4f6f8 28%,#c7d0d9 55%,#8e9aa6 75%,#b6c0ca 100%)}
.hero-fade{position:absolute;left:0;top:0;width:471px;height:360px;
  background:linear-gradient(90deg,rgba(255,255,255,.95) 0%,rgba(255,255,255,.6) 40%,rgba(255,255,255,0) 70%)}
.red-panel{position:absolute;left:0;top:250px;width:471px;height:328px;
  background:linear-gradient(180deg,rgba(226,50,50,0) 0%,rgba(226,50,50,.85) 60px,var(--red) 110px,#d92c2c 100%)}
.front .brand{left:34px;top:15px}
.headline{position:absolute;left:33px;top:110px;font-weight:800;font-size:25px;line-height:28px;color:var(--red)}
.subhead{position:absolute;left:33px;top:308px;font-weight:600;font-size:19px;line-height:25px;color:var(--white)}
.intro{position:absolute;color:var(--white)}
.intro h3{font-weight:700;font-size:10.5px;line-height:15px;margin-bottom:2px}
.intro p{font-weight:400;font-size:8.2px;line-height:11.7px;color:#fbe3e3}
.intro--what{left:33px;top:387px;width:195px}
.intro--hosted{left:33px;top:454px;width:200px}
.intro--why{left:258px;top:387px;width:180px}
.footer-line{position:absolute;left:0;bottom:0;width:100%;height:32px;display:flex;align-items:center;justify-content:center;font-size:5.6px;font-weight:700;color:var(--dark);white-space:nowrap}
.footer-line .tag{color:var(--red);margin:0 3px}

/* back */
.info-photo{position:absolute;left:0;top:0;width:471px;height:275px;
  background:radial-gradient(ellipse at 50% 60%,#d9d6d0 0%,#e8e6e2 45%,#eeeeee 100%)}
.back .brand{right:33px;top:15px}
.benefits{position:absolute;left:0;top:0}
.benefit{position:absolute;font-family:'Roboto Condensed',sans-serif}
.benefit h4{font-weight:600;font-size:8.4px;line-height:11px}
.benefit p{font-size:5.5px;line-height:8px;color:#333}
.b-mobility{left:224px;top:38px;width:92px}
.b-mobility h4{color:var(--amber)}
.b-routing{left:52px;top:101px;width:85px}
.b-routing h4{color:var(--orange)}
.b-smb{left:311px;top:102px;width:112px}
.b-smb h4{color:var(--green)}
.b-maint{left:80px;top:219px;width:140px}
.b-maint h4{color:var(--navy)}
.b-geo{left:281px;top:219px;width:125px}
.b-geo h4{color:var(--teal)}

.details{position:absolute;top:284px;font-size:8.2px;line-height:11.2px;color:var(--ink)}
.details--left{left:43px;width:190px}
.details--right{left:241px;width:190px}
.lead{font-weight:700;margin-bottom:7px}
.points{list-style:none}
.points li{position:relative;padding-left:13px;margin-bottom:7px}
.points li::before{content:"";position:absolute;left:1px;top:4px;width:3.5px;height:3.5px;border-radius:50%;background:var(--ink)}
.points strong{font-weight:700}
.points .block{display:block}
.services-intro{margin-top:9px}
.ticks{list-style:none;margin-top:2px}
.ticks li{position:relative;padding-left:13px;line-height:13px}
.ticks svg{position:absolute;left:1px;top:4px}
.cta{position:absolute;left:0;top:545px;width:100%;height:32px;background:var(--dark);color:var(--white);font-size:9px;line-height:10.5px;text-align:center;padding-top:5px}
.cta strong{font-weight:700}
.footer-band{position:absolute;left:0;top:577px;width:100%;height:33px;background:var(--red);display:flex;align-items:center;justify-content:center;font-size:5.6px;font-weight:700;color:var(--white);white-space:nowrap}
.footer-band .tag{color:var(--dark);margin:0 3px}
</style>
</head>
<body>

<section class="page page--front front">
  <div class="hero-photo" role="img" aria-label="Photo of an office desk phone with a headset resting beside it"></div>
  <div class="hero-fade"></div>
  <div class="red-panel"></div>
  <div class="brand"><span class="brand__dot"></span>KestrelVoice</div>
  <h1 class="headline">Is it time<br>for a better<br>phone system?</h1>
  <h2 class="subhead">Americas most popular<br>phone system - Voice Over IP (VOIP)</h2>
  <div class="intro intro--what">
    <h3>What is VOIP?</h3>
    <p>VOIP offers a very versatile, low-cost solution for phones and communication that can easily scale with the growth of your business.</p>
  </div>
  <div class="intro intro--hosted">
    <h3>Hosted VoIP Phone System</h3>
    <p>A fully featured phone system that runs in the cloud with an easy-access online portal for administration and user management. VOIP includes routing work-flows, music on hold, call queues, web phone app and much more.</p>
  </div>
  <div class="intro intro--why">
    <h3>Why Choose Our Hosted VOIP Phone Service?</h3>
    <p>At Kestrel Voice our business phone service is best-of-breed that utilizes redundant servers in geographically disperse regions throughout the country to ensure high reliability and sound quality.</p>
  </div>
  <div class="footer-line">Kestrel Voice 1200 Harbor View Drive Bayport, VA 23000 <span class="tag">| TF</span> 888-555-0142 <span class="tag">| PH</span> 757-555-0188 FX 757-555-0199</div>
</section>

<section class="page page--back back">
  <div class="info-photo" role="img" aria-label="Faded photo of a desk phone and headset behind the benefits graphic"></div>
  <div class="brand"><span class="brand__dot"></span>KestrelVoice</div>

  <svg class="benefits" width="471" height="275" viewBox="0 0 471 275" aria-hidden="true">
    <!-- rings -->
    <g fill="none" stroke-width="2.2" stroke-linecap="round">
      <circle cx="220" cy="150" r="58" stroke="var(--orange)" stroke-dasharray="85 280" transform="rotate(200 220 150)"/>
      <circle cx="220" cy="150" r="58" stroke="var(--amber)" stroke-dasharray="85 280" transform="rotate(290 220 150)"/>
      <circle cx="220" cy="150" r="58" stroke="var(--green)" stroke-dasharray="80 290" transform="rotate(15 220 150)"/>
      <circle cx="220" cy="150" r="52" stroke="var(--teal)" stroke-dasharray="120 240" transform="rotate(60 220 150)"/>
      <circle cx="220" cy="150" r="52" stroke="var(--navy)" stroke-dasharray="110 250" transform="rotate(160 220 150)"/>
    </g>
    <g stroke-width="1.4">
      <line x1="150" y1="120" x2="174" y2="127" stroke="var(--orange)"/>
      <line x1="220" y1="80" x2="220" y2="92" stroke="var(--amber)"/>
      <line x1="300" y1="110" x2="280" y2="124" stroke="var(--green)"/>
      <line x1="190" y1="208" x2="180" y2="225" stroke="var(--navy)"/>
      <line x1="258" y1="200" x2="276" y2="214" stroke="var(--teal)"/>
    </g>
    <text x="190" y="140" font-family="Roboto Condensed, sans-serif" font-weight="600" font-size="7" fill="var(--navy)">Benefits of</text>
    <text x="189" y="163" font-family="Montserrat, sans-serif" font-weight="800" font-size="22" fill="var(--grey)">VoIP</text>
    <text x="211" y="171" font-family="Montserrat, sans-serif" font-weight="600" font-size="5.5" fill="var(--red)">Telephony</text>

    <!-- mobility phone -->
    <rect x="200" y="41" width="14" height="24" rx="2" fill="none" stroke="var(--amber)" stroke-width="1.6"/>
    <line x1="205" y1="61" x2="209" y2="61" stroke="var(--amber)" stroke-width="1.2"/>

    <!-- routing nodes -->
    <g stroke="var(--orange)" stroke-width="1.3" fill="none">
      <circle cx="96" cy="78" r="6"/>
      <circle cx="96" cy="62" r="3"/><circle cx="110" cy="70" r="3"/><circle cx="110" cy="88" r="3"/>
      <circle cx="82" cy="88" r="3"/><circle cx="82" cy="70" r="3"/>
      <line x1="96" y1="72" x2="96" y2="65"/><line x1="101" y1="75" x2="108" y2="71"/>
      <line x1="101" y1="82" x2="108" y2="86"/><line x1="91" y1="82" x2="84" y2="86"/>
      <line x1="91" y1="75" x2="84" y2="71"/>
    </g>

    <!-- people group -->
    <g fill="var(--green)">
      <circle cx="358" cy="66" r="3.5"/><circle cx="346" cy="72" r="3"/><circle cx="370" cy="72" r="3"/>
      <rect x="352" y="71" width="12" height="15" rx="2"/>
      <rect x="341" y="76" width="9" height="12" rx="2"/>
      <rect x="366" y="76" width="9" height="12" rx="2"/>
    </g>

    <!-- gear -->
    <g transform="translate(119 108)">
      <circle r="16" fill="none" stroke="var(--navy)" stroke-width="3" stroke-dasharray="4 2.3"/>
      <circle r="11" fill="none" stroke="var(--navy)" stroke-width="3"/>
      <circle r="4.5" fill="var(--navy)"/>
    </g>

    <!-- pin -->
    <g transform="translate(326 180)">
      <path d="M0 -17 a6.5 6.5 0 0 1 6.5 6.5 c0 5 -6.5 12 -6.5 12 s-6.5 -7 -6.5 -12 a6.5 6.5 0 0 1 6.5 -6.5z" fill="var(--teal)"/>
      <circle cy="-10.5" r="2.5" fill="#fff"/>
      <rect x="-20" y="4" width="40" height="3" rx="1.5" fill="var(--teal)" opacity=".7"/>
      <rect x="-14" y="9" width="28" height="3" rx="1.5" fill="var(--teal)" opacity=".5"/>
    </g>
  </svg>

  <div class="benefit b-mobility"><h4>Mobility</h4><p>VoIP allows for mobility Kestrel business soft phone is available for dekstop or mobile phone, making your office portable.</p></div>
  <div class="benefit b-routing"><h4>Call routing &amp; Automation</h4><p>While we may complain about thede systems at times, think back to before when calls would just go to viecemail, or, even worse, ring perpetually.</p></div>
  <div class="benefit b-smb"><h4>Even playing field for SMBs</h4><p>One of the best things about VoIP is that evens the playing field for even the smallest companies. VoIP is scalable and can give a small company just what they need and then grow with them.</p></div>
  <div class="benefit b-maint"><h4>Less maintenance</h4><p>Hosted VoIP is managed, at least partially, if not fully, but the service provider. This means no need for maintenance or big IT teams for your company</p></div>
  <div class="benefit b-geo"><h4>Even playing field for SMBs</h4><p>VoIP can give you local phone numbers and inexpensive long-distance calling, breaking traditional geographic boundaries.</p></div>

  <div class="details details--left">
    <p class="lead">Additionally, people appreciate the following…</p>
    <ul class="points">
      <li><strong>Competitive pricing:</strong> Low flat-fee pricing for unlimited local and long-distance phone service. Our pricing includes an extensive feature list that includes routing by time-frames, easy to create work-flows, company greeting and menu-list (Auto Attendant), ring-all or find the available staff member, call-center reporting and more.</li>
      <li><strong class="block">No set-up fees!</strong>Let us do the heavy-lifting. We will plan and configure your dream phone system as part of our service.</li>
      <li><strong class="block">Quality phones</strong>We include business phones by Tonara and we support most VOIP phone manufacturers including Veltro, Tonara, Sonique, Arcline and many others.</li>
    </ul>
  </div>

  <div class="details details--right">
    <ul class="points">
      <li><strong class="block">Call Center</strong>Track stats on call-center flow, abandoned calls, voicemails, hold times, and more. Our granular reports and call center manager portal allow you to manage your team better than ever.</li>
      <li><strong class="block">Audio &amp; Video Conferencing</strong>Audio conferencing and video conferencing are a rising need for modern business. Remove the need for multiple applications and handle all client communication under one platform.</li>
    </ul>
    <p class="services-intro">We are a full-service VOIP phone system vendor. Our services include…</p>
    <ul class="ticks">
      <li><svg width="6" height="5" viewBox="0 0 6 5"><path d="M.5 2.6 2.2 4.2 5.5.6" fill="none" stroke="var(--ink)" stroke-width=".9"/></svg>Planning</li>
      <li><svg width="6" height="5" viewBox="0 0 6 5"><path d="M.5 2.6 2.2 4.2 5.5.6" fill="none" stroke="var(--ink)" stroke-width=".9"/></svg>Phone sales</li>
      <li><svg width="6" height="5" viewBox="0 0 6 5"><path d="M.5 2.6 2.2 4.2 5.5.6" fill="none" stroke="var(--ink)" stroke-width=".9"/></svg>installation</li>
      <li><svg width="6" height="5" viewBox="0 0 6 5"><path d="M.5 2.6 2.2 4.2 5.5.6" fill="none" stroke="var(--ink)" stroke-width=".9"/></svg>support</li>
      <li><svg width="6" height="5" viewBox="0 0 6 5"><path d="M.5 2.6 2.2 4.2 5.5.6" fill="none" stroke="var(--ink)" stroke-width=".9"/></svg>management</li>
    </ul>
  </div>

  <div class="cta">Call us direct at <strong>757-555-0123</strong> to get a FREE consultation or demonstration<br>with absolutely no pressure or obligation.</div>
  <div class="footer-band">Kestrel Voice 1200 Harbor View Drive Bayport, VA 23000 <span class="tag">| TF</span> 888-555-0142 <span class="tag">| PH</span> 757-555-0188 FX 757-555-0199</div>
</section>

</body>
</html>
```